Commercial Real Estate Company Needs Website Redesign

Velcaro is a commercial real estate firm that is based in San Diego, but has offices and properties across the U.S. The current website was completed almost 3 years ago and is need of a refresh. We will rework the existing Wordpress CMS system, but require a new design. We have a great programmer who can take the design into wordpress. I need a design template for each page types, There are are approximately 20 pages for each section of our site. There are 4 Sections: Corporate, Hospitality, Commercial/Residential, and Receiver/Bankruptcy. See attached creative brief for the initial pages we would like drafted.

Industry/Entity Type

Real Estate

```html
<!DOCTYPE html>
<html lang="en">
<head>
<meta charset="utf-8">
<title>Velcaro — Who We Are</title>
<link href="https://fonts.googleapis.com/css2?family=Open+Sans:wght@400;600;700&family=Raleway:wght@300;400;600;700&display=swap" rel="stylesheet">
<style>
  :root{
    --page:#1f2429;
    --top-strip:#15181b;
    --nav:#3b3f44;
    --nav-home:#4a4e53;
    --orange:#f7a21b;
    --orange-light:#fbb53a;
    --ink:#f2f2f2;
    --muted:#5d656d;
    --sidebar-frame:#34383c;
    --sidebar:#15181b;
    --rule:#2b2f33;
    --footer:#353a40;
    --footer-text:#8b9197;
    --bottom:#24272b;
    --blue-icon:#2c7fd1;
  }
  *{box-sizing:border-box;margin:0;padding:0}
  html,body{width:986px;height:1200px;overflow:hidden;background:var(--page)}
  body{position:relative;font-family:"Open Sans",sans-serif;color:var(--ink)}
  .abs{position:absolute}

  .top-strip{left:0;top:0;width:986px;height:5px;background:var(--top-strip)}
  .hero-band{left:0;top:182px;width:986px;height:250px;
    background:linear-gradient(#5d6166,#3c4044);border-top:1px solid #c9ccd0}

  /* header */
  .brand{left:83px;top:36px;display:flex;align-items:center;gap:10px}
  .brand-mark{width:14px;height:14px;background:var(--orange);display:block}
  .brand-name{font-family:"Open Sans",sans-serif;font-weight:600;font-size:26px;color:#ffffff;line-height:1}
  .call{left:640px;top:42px;display:flex;align-items:center;gap:8px;font-size:14px;font-weight:600;color:#d8dadc}
  .social{left:838px;top:41px;display:flex;gap:5px}
  .social span{width:18px;height:18px;display:block}

  /* navigation */
  .main-nav{left:83px;top:101px;width:822px;height:31px;background:var(--nav);border-radius:2px;display:flex;align-items:stretch;font-size:12px;font-weight:600}
  .nav-home{width:47px;background:var(--nav-home);display:flex;align-items:center;justify-content:center;border-radius:2px 0 0 2px}
  .nav-item{display:flex;align-items:center;justify-content:center;color:#fff}
  .nav-item.active{background:linear-gradient(var(--orange-light),var(--orange));color:#2a2016}

  /* slider */
  .slider{left:83px;top:150px;width:580px;height:320px;background:#3f4347;padding:4px}
  .slide-photo{width:100%;height:100%;
    background:radial-gradient(ellipse at 45% 35%,#d8c79a 0%,#a88f5e 40%,#4d3b25 80%,#1e1710 100%)}
  .caption{left:123px;top:367px;width:504px;height:66px;background:rgba(247,162,27,.88);
    border-right:5px solid #f2eee6;display:flex;align-items:center;justify-content:center;text-align:center;
    font-size:18px;line-height:23px;color:#2b1f10}
  .pager-btn{top:456px;height:21px;width:47px;background:#2b2e31;font-size:8px;color:#e0e0e0;display:flex;align-items:center;justify-content:center}
  .pager-dots{left:330px;top:450px;width:100px;height:32px;background:linear-gradient(#3c4044,#1d2023);display:flex;align-items:center;justify-content:center;gap:8px;box-shadow:0 3px 6px rgba(0,0,0,.5)}
  .pager-dots i{width:8px;height:8px;border-radius:50%;background:#55595d;display:block}
  .pager-dots i.on{width:11px;height:11px;background:var(--orange)}

  /* sidebar */
  .side-panel{left:678px;top:150px;width:227px;height:320px;background:var(--sidebar-frame);padding:5px}
  .side-inner{width:100%;height:100%;background:var(--sidebar);position:relative}
  .side-links{list-style:none;padding:0 6px}
  .side-links li{height:40px;border-bottom:1px solid var(--rule);display:flex;align-items:center;font-size:12px;color:#b9bdc1;padding-left:10px}
  .side-links li::before{content:"›";margin-right:12px;color:#9aa0a5;font-size:12px}
  .side-btn{position:absolute;left:14px;width:189px;height:32px;display:flex;align-items:center;gap:14px;padding-left:12px;font-size:10px;font-weight:700}
  .btn-subscribe{top:221px;background:linear-gradient(var(--orange-light),var(--orange));color:#2a1b08}
  .btn-consult{top:262px;background:linear-gradient(#3c4146,#24282c);color:#fff}

  /* services */
  .service{top:513px;width:240px;text-align:center}
  .service-photo{width:134px;height:134px;border-radius:50%;margin:0 auto;box-shadow:0 4px 10px rgba(0,0,0,.5)}
  .service h2{margin-top:23px;font-size:16px;font-weight:600;color:#c7cacd;letter-spacing:.2px}
  .service h2.accent{color:var(--orange)}
  .service p{margin-top:4px;font-size:11.3px;line-height:14.6px;color:var(--muted);text-align:justify;text-align-last:center}

  /* footer */
  .footer{left:0;top:859px;width:986px;height:279px;background:var(--footer);font-family:"Raleway",sans-serif}
  .footer h3{position:absolute;top:40px;font-weight:300;font-size:17px;color:#fff}
  .footer h3 b{font-weight:700}
  .footer-copy{position:absolute;font-size:9px;line-height:15.2px;color:var(--footer-text)}
  .news-date{position:absolute;left:296px;top:86px;width:43px;text-align:center}
  .news-day{font-size:16px;font-weight:700;color:#fff;padding-bottom:3px;border-bottom:1px solid var(--blue-icon)}
  .news-month{font-size:8px;letter-spacing:1.5px;color:#fff;margin-top:5px}
  .news-title{position:absolute;left:352px;top:86px;font-size:13px;line-height:20px;color:#fff}
  .news-arrows{position:absolute;left:296px;top:205px;display:flex;gap:8px}
  .client{position:absolute;left:538px;font-family:"Open Sans",sans-serif;font-weight:700;font-size:14px;color:#d6dadd;display:flex;align-items:center;gap:6px}
  .client i{width:10px;height:10px;background:#6e7a88;display:block}
  .contact-icon{position:absolute;left:720px}

  .bottom-bar{left:0;top:1138px;width:986px;height:62px;background:var(--bottom);font-family:"Raleway",sans-serif}
  .copyright{position:absolute;left:82px;top:20px;font-size:9.5px;color:#9a9ea2}
  .copyright b{color:#fff;font-weight:600}
  .bottom-links{position:absolute;right:81px;top:19px;font-size:10.5px;font-weight:600;color:#fff;display:flex;gap:8px}
  .bottom-links span.sep{color:#777c81;font-weight:400}
</style>
</head>
<body>
  <div class="abs top-strip"></div>
  <div class="abs hero-band"></div>

  <header>
    <div class="abs brand">
      <i class="brand-mark"></i>
      <div class="brand-name">Velcaro</div>
    </div>
    <div class="abs call">
      <svg width="12" height="17" viewBox="0 0 12 17"><path d="M3 1 L6 5 L4 7 Q5 11 8 13 L10 11 L12 14 L9 16 Q1 12 1 3 Z" fill="#d8dadc"/></svg>
      Call: 619 - 555 - 0148
    </div>
    <div class="abs social" aria-label="Social links">
      <span style="background:#1d7bb3"></span>
      <span style="background:#37b4e8"></span>
      <span style="background:#c9cdd1"></span>
    </div>
  </header>

  <nav class="abs main-nav">
    <div class="nav-home">
      <svg width="14" height="12" viewBox="0 0 14 12"><path d="M7 0 L14 6 L12 6 L12 12 L8.5 12 L8.5 8 L5.5 8 L5.5 12 L2 12 L2 6 L0 6 Z" fill="#e5e5e5"/></svg>
    </div>
    <div class="nav-item active" style="width:115px">Who We Are</div>
    <div class="nav-item" style="width:142px">What We Do</div>
    <div class="nav-item" style="width:133px">What We've Done</div>
    <div class="nav-item" style="width:107px">Contact Us</div>
    <div class="nav-item" style="width:114px">Velcaro Home</div>
  </nav>

  <section class="abs slider">
    <div class="slide-photo" role="img" aria-label="Hotel bedroom with lamps, cushions and a white bed"></div>
  </section>
  <div class="abs caption">Contact us today. Let you put our expertise to work<br>for you.</div>
  <div class="abs pager-btn" style="left:282px">PREV</div>
  <div class="abs pager-dots"><i></i><i class="on"></i><i></i><i></i><i></i></div>
  <div class="abs pager-btn" style="left:431px">NEXT</div>

  <aside class="abs side-panel">
    <div class="side-inner">
      <ul class="side-links">
        <li>Portfolio Map</li>
        <li>Buyer Registration</li>
        <li>Properties for Sale</li>
        <li>Industry Updates</li>
        <li>Velcaro Deskbook</li>
      </ul>
      <div class="side-btn btn-subscribe">
        <svg width="18" height="12" viewBox="0 0 18 12"><rect x="0.5" y="0.5" width="17" height="11" fill="#2a1b08"/><path d="M1 1 L9 7 L17 1" stroke="#f7a21b" fill="none"/></svg>
        SUBSCRIBE TO NEWSLETTER
      </div>
      <div class="side-btn btn-consult">
        <svg width="12" height="14" viewBox="0 0 12 17"><path d="M3 1 L6 5 L4 7 Q5 11 8 13 L10 11 L12 14 L9 16 Q1 12 1 3 Z" fill="#fff"/></svg>
        FREE CONSULTATION
      </div>
    </div>
  </aside>

  <section class="abs service" style="left:83px">
    <div class="service-photo" role="img" aria-label="Portrait of a smiling property owner in a suit" style="background:linear-gradient(160deg,#d9d6d0,#6b6358 60%,#2a2624)"></div>
    <h2 class="accent">FOR OWNERS</h2>
    <p>Aliquam erat theme the is volutpat. Duis volutpat bibendum purus faucibus tincidunt. Maecenas aliquet varius risus nec dapibus. Ut posuere vehicula nisl nec mollis. Ut tellus tellus, dignissim at eros vehicula, consectetur placerat magna. Proin ornare scelerisque ipsum a convallis.</p>
  </section>
  <section class="abs service" style="left:374px">
    <div class="service-photo" role="img" aria-label="Businesswoman reviewing documents by a city window" style="background:linear-gradient(160deg,#c9ced4,#7e8790 55%,#2f3338)"></div>
    <h2>FOR BUYERS/DEVELOPERS</h2>
    <p>Aliquam erat theme the is volutpat. Duis volutpat bibendum purus faucibus tincidunt. Maecenas aliquet varius risus nec dapibus. Ut posuere vehicula nisl nec mollis. Ut tellus tellus, dignissim at eros vehicula,</p>
  </section>
  <section class="abs service" style="left:665px">
    <div class="service-photo" role="img" aria-label="Silhouettes of business people meeting before a bright window" style="background:radial-gradient(circle at 50% 45%,#f4f6f8,#aab3bb 55%,#3b4147)"></div>
    <h2>FOR LENDERS</h2>
    <p>Aliquam erat theme the is volutpat. Duis volutpat bibendum purus faucibus tincidunt. Maecenas aliquet varius risus nec dapibus. Ut posuere vehicula nisl nec mollis. Ut tellus tellus, dignissim at eros vehicula, consectetur placerat magna.</p>
  </section>

  <footer class="abs footer">
    <h3 style="left:83px">Why Choose Us</h3>
    <p class="footer-copy" style="left:82px;top:86px;width:183px">Donec leo ipsum, suscipit et consectetur non, consectetur dapibus turpis. Phasellus mauris nulla, condimentum nec ultricies mattis, tincidunt a leo. Phasellus nec dui placerat, dictum purus id, sollicitudin ipsum. Sed eget molestie lectus.</p>

    <h3 style="left:295px">Latest <b>News</b></h3>
    <div class="news-date"><div class="news-day">03</div><div class="news-month">DEC, 13</div></div>
    <div class="news-title">Cum Sociis Natoque<br>Penatibus Et Magnis...</div>
    <p class="footer-copy" style="left:296px;top:136px;width:190px">Suspendisse pulvinar felis eu consequat mattis. Proin euismod placerat consectetur. Proin dapibus ante id eros...</p>
    <div class="news-arrows">
      <svg width="21" height="21" viewBox="0 0 21 21"><circle cx="10.5" cy="10.5" r="9.5" stroke="#fff" stroke-width="1.5" fill="none"/><path d="M12 7 L8.5 10.5 L12 14" stroke="#fff" stroke-width="1.3" fill="none"/></svg>
      <svg width="21" height="21" viewBox="0 0 21 21"><circle cx="10.5" cy="10.5" r="9.5" stroke="#fff" stroke-width="1.5" fill="none"/><path d="M9 7 L12.5 10.5 L9 14" stroke="#fff" stroke-width="1.3" fill="none"/></svg>
    </div>

    <h3 style="left:531px">Our Clients</h3>
    <div class="client" style="top:95px"><i></i>HARLOW GROUP</div>
    <div class="client" style="top:145px"><i></i>DENMORE CAPITAL</div>

    <h3 style="left:720px">Contacts</h3>
    <svg class="contact-icon" style="top:93px" width="11" height="15" viewBox="0 0 11 15"><path d="M5.5 0 A5.5 5.5 0 0 1 11 5.5 C11 9 5.5 15 5.5 15 C5.5 15 0 9 0 5.5 A5.5 5.5 0 0 1 5.5 0 Z" fill="var(--blue-icon)"/><circle cx="5.5" cy="5.5" r="2" fill="#353a40"/></svg>
    <p class="footer-copy" style="left:721px;top:108px;width:190px">48 Harbor Lane, Seabrook Bay 4021<br>Australia</p>
    <svg class="contact-icon" style="top:157px" width="13" height="13" viewBox="0 0 12 17"><path d="M3 1 L6 5 L4 7 Q5 11 8 13 L10 11 L12 14 L9 16 Q1 12 1 3 Z" fill="var(--blue-icon)"/></svg>
    <p class="footer-copy" style="left:721px;top:170px">+1 555 010 42</p>
    <svg class="contact-icon" style="top:207px" width="17" height="12" viewBox="0 0 17 12"><rect width="17" height="12" rx="1" fill="var(--blue-icon)"/><path d="M1 1 L8.5 7 L16 1" stroke="#353a40" stroke-width="1.3" fill="none"/></svg>
    <p class="footer-copy" style="left:721px;top:224px">hello@velcaro-example.com</p>
  </footer>

  <div class="abs bottom-bar">
    <div class="copyright">© Copyright 2014 by <b>Velcaro</b>. All Rights Reserved.</div>
    <div class="bottom-links"><span>HOME</span><span class="sep">/</span><span>FAQ</span><span class="sep">/</span><span>CONTACTS</span></div>
  </div>
</body>
</html>
```